1700% Campground Membership fee increase info graphic

This will illustrate a 1700% rate increase by the Quellridge Area Visitor Bureau's suddenly imposed on our area's small family operated campgrounds. We are sending this with a press release that will have a political cartoon. So that part is playful - so we want this part to be a bit more serious. We need an info graphic that shows the scale of what a 1700% increase means. Perhaps a photo realistic dollar bill on one pile labeled 2017 (represents rates that year), and a huge pile of cash (1700% bigger) labeled 2018. The labels need to identify that this represents the percentage of rate increase imposed by the Quellridge Area Visitor's Bureau (their full name) on Quellridge's Family Campgrounds. The increase should be labeled (or perhaps the whole graphic) as "Campground Membership Fees." It can also be a 3D graphic, but we want it to be polished, but also an attention getter, so if that means some pro but ragged elements, so be it. A chart like something from Excel won't work (to easy to skim over) unless it is something really striking looking. I have attached an Excel chart just for reference, but we want something that get's the same information across in a bit more of an attention getting way. The actual fee increase is based on a 2017 fee of $560 and an increase for 2018 to $10,500. So that could be part of it. I have attached a rough of that idea - again it is just there for the concept, don't let our poor drawing distract you from your good idea. Unless you have a better idea, I am thinking a limited pallette might be best as the cartoon for this release will be in color. However, if you have a great full color idea- please let me see it. Green means money, so I would like that as part of the graphic.

This will hopefully appear in newspapers and magazines

• Something easily read, up to date - you pick

• It should be clear from a glance what it is. People skim, it is ok if they have to give it a good look for details.
• perhaps photo realistic money on the stack
• Excel looking graphics

```html
<!DOCTYPE html>
<html lang="en">
<head>
<meta charset="utf-8">
<title>Campground Membership Fees</title>
<link rel="stylesheet" href="https://fonts.googleapis.com/css2?family=Oswald:wght@700&family=Montserrat:wght@800&family=Alfa+Slab+One&family=Cinzel:wght@400&display=swap">
<style>
  :root {
    --money-green: #44b649;
    --bar-green: #8bbb3e;
    --bar-shade: #6f9a2c;
    --ink: #111111;
    --axis-grey: #c9cdd2;
    --axis-line: #8a8f96;
    --alert-red: #ea4426;
    --burst-green: #8cc63f;
    --burst-yellow: #d9e021;
    --paper: #ffffff;
  }
  html, body {
    margin: 0;
    padding: 0;
    width: 1200px;
    height: 1200px;
    overflow: hidden;
    background: var(--paper);
  }
  .infographic { display: block; width: 1200px; height: 1200px; }
  .headline { font-family: "Oswald", "Arial Narrow", sans-serif; font-weight: 700; fill: var(--money-green); }
  .amount, .year, .source { font-family: "Montserrat", "Arial", sans-serif; font-weight: 800; fill: var(--ink); }
  .percent { font-family: "Alfa Slab One", "Rockwell", serif; fill: var(--alert-red); stroke: var(--ink); stroke-width: 3; paint-order: stroke; }
  .increase-word { font-family: "Cinzel", "Times New Roman", serif; fill: var(--ink); }
  .axis-band { fill: var(--axis-grey); stroke: var(--axis-line); stroke-width: 1.5; }
  .bar-front { fill: var(--bar-green); stroke: var(--ink); stroke-width: 2; }
  .bar-side { fill: var(--bar-shade); stroke: var(--ink); stroke-width: 2; }
  .bar-top { fill: #f2f2f2; stroke: var(--ink); stroke-width: 2; }
  .growth-arrow { fill: var(--bar-green); stroke: var(--ink); stroke-width: 2; }
</style>
</head>
<body>
<svg class="infographic" viewBox="0 0 1200 1200" xmlns="http://www.w3.org/2000/svg">
  <defs>
    <radialGradient id="burstFill" cx="50%" cy="50%" r="55%">
      <stop offset="0%" stop-color="#f15a29"/>
      <stop offset="40%" stop-color="var(--burst-yellow)"/>
      <stop offset="100%" stop-color="var(--burst-green)"/>
    </radialGradient>
  </defs>

  <!-- Headline -->
  <text class="headline" x="600" y="206" text-anchor="middle" font-size="100" textLength="936" lengthAdjust="spacingAndGlyphs">CAMPGROUND MEMBERSHIP FEES</text>

  <!-- Chart axes -->
  <g class="chart-axes">
    <rect class="axis-band" x="114" y="440" width="20" height="640"/>
    <path class="axis-band" d="M100 438 L128 392 L150 436 L124 428 Z"/>
    <rect class="axis-band" x="116" y="1056" width="562" height="18"/>
    <path class="axis-band" d="M668 1046 L694 1066 L652 1088 L664 1066 Z"/>
  </g>

  <!-- Growth arrow -->
  <path class="growth-arrow" d="M198 1042 C 290 960, 380 820, 420 618 L 382 622 L 450 556 L 478 642 L 440 626 C 410 820, 320 970, 198 1042 Z"/>

  <!-- 2017 bar -->
  <g class="bar bar-2017">
    <polygon class="bar-top" points="254,1014 266,998 312,998 298,1014"/>
    <polygon class="bar-side" points="298,1014 312,998 312,1060 298,1074"/>
    <rect class="bar-front" x="254" y="1014" width="44" height="60"/>
  </g>

  <!-- 2018 bar -->
  <g class="bar bar-2018">
    <polygon class="bar-top" points="496,546 520,516 576,516 558,546"/>
    <polygon class="bar-side" points="558,546 576,516 576,1048 558,1070"/>
    <rect class="bar-front" x="496" y="546" width="62" height="524"/>
  </g>

  <!-- Values -->
  <text class="amount" x="158" y="912" font-size="46">$ 560</text>
  <text class="amount" x="392" y="468" font-size="62" textLength="270" lengthAdjust="spacingAndGlyphs">$ 10,500</text>

  <!-- Years -->
  <text class="year" x="306" y="1126" font-size="34" text-anchor="middle">2017</text>
  <text class="year" x="510" y="1126" font-size="34" text-anchor="middle">2018</text>

  <!-- Comic exclamation burst -->
  <ellipse role="img" aria-label="Comic-style starburst with the exclamation WOW" cx="890" cy="560" rx="262" ry="190" fill="url(#burstFill)"/>

  <!-- Increase figure -->
  <text class="percent" x="920" y="872" font-size="128" text-anchor="middle" textLength="256" lengthAdjust="spacingAndGlyphs">1700%</text>
  <text class="increase-word" x="918" y="926" font-size="54" text-anchor="middle" textLength="252" lengthAdjust="spacingAndGlyphs">INCREASE</text>

  <!-- Source -->
  <text class="source" x="922" y="1016" font-size="34" text-anchor="middle" textLength="330" lengthAdjust="spacingAndGlyphs">QUELLRIDGE AREA</text>
  <text class="source" x="922" y="1070" font-size="34" text-anchor="middle" textLength="354" lengthAdjust="spacingAndGlyphs">VISITOR BUREAU'S</text>
</svg>
</body>
</html>
```